Mobile Marketing Business needs a UNIQUE web design that makes users stop, adore and engage!

Unique web design for a new division of our company. Based in Los Angeles, TornaCell is a mobile marketing company offering mobile optimized websites, sms marketing, strategic and analytic consultation services. We are a b2b model targeting a wide range of industries and business sizes. Our parent company is Harbor Reach Online. Tornacell needs to reflect a progressive nature, confidence, and experience - yet affordable to any business that wants to reach the mobile consumer. We want to avoid a dark website or one that is too bland. The colors should be strong, yet not overly so.

Layout should be clean, focused, - avoiding a cluttered home page. Visitors should recognize WE ARE mobile marketing - it should resonate that WE differ from competitors - Site design should resonate our brand! We've noticed competitors sites start to look and feel like the same - where the visitor may quickly exit from the home page or first inner page. There are some sites that differ which we've listed below.

The audience will range from sophisticated marketers to a local business operator who is not web savvy. The site should welcome all - not intimidate some while wowing others. We understand it's difficult for websites to be a "one size fits all" - but in reviewing competitive sites, it's apparent no one site really leaves any key impression. We'd like Tornacell to be the one.

The site should invite user to engage with the site and compel them to contact us for a demo for a better understanding of how mobiele marketing is the ultimate one 2 one sales channel that can help them improve gross sales.

Site should not be "dark" which requires using white font - we do not want "wild" or "fluorescent" colors. A tasteful, classic balance of colors that provides a comfortable experience to engage.

We realize this challenge seems .. well extremely challenging but we're quite confident there is a "design ninja" lurking out there. Are YOU the one?

Happy to provide more details and info as needed.

Sample sites that we like and feel are unique to the industry and also a site that we feel is quite basic:

www.palvexagency.example - clever use of banner area and using a slider to present services. However, labeling the sliders as such is a little difficult to read.

www.brindlecell.example - clean, classic, minimalistic. Perhaps too minimal for our need but we like it. Nice use of the varying sizes and treatment of 3 promo boxes under main banner. Inner page layout is nice.

www.quarvelworks.example - clever, unique. Love the call to action box (adjacent to phone) offering 3 options for next steps. Inner pages are well designed - overall site is clean, easy to read and merchandises offerings effectively.

www.tallpinegrovemedia.example - clean, well merchandised but home page is a bit too cluttered. good use of colors, inner page layout is simple but effective.

www.wextaline.example - clean, simple easy to follow.

www.plomadix.example - pretty basic site - in fact, you could probably replace the logo with another marketing company, etc. and the site would most likely work. We would prefer to avoid this stigma for TornaCell!!

NOTE: our logo uses a bright green that may limit it's use for mostly accents, etc. We like the contrast of colors used on www.zendravo.example and www.kettlefold.example/ using the dark gray background and other colors to bring some life.

If you google "mobile marketing company", "mobile marketing services", "text messaging services", etc.. you'll notice 2 distinctive categories: amazing - like what the heck were they thinking.. and yawn - like here's another one that looks like the other..

Thank you everyone for the submissions - while they are nice, I have to say they fall into the category we were hoping to avoid (yawn, this one looks like all the other company sites)..  

Please do review the brief thoroughly - we're available if you need a specific issue addressed.  

We're still hoping a design ninja surfaces and provides a comp that makes us go "WOW'..  

cheers and good luck!

Thanks for your participation -  please stay tuned for an update to the brief along with some copy to populate the home page.  

Also... keep an eye on the project award..  we'll be increasing it after posting updates!

cheers.

UPDATE!  We have INCREASED the award in hopes of inspiring you great designers to entice your imagination and creative genetics!

PLEASE feel free to ask for further clarification or even if you want to run something by before submitting a design.  

We also have several other projects and would certainly consider those designers that truly impressed us.

As promised we're adding a bit more detail to this project.  The project requires a home and inner page layout but would like to start with the home page first.   We would also like to have a blog that differs a bit but retain some core elements of the site design.

This is a new design - our desire is to launch a website bearing an effective yet distinctive look.  Again, if you google "mobile marketing services", "mobile marketing company/companies", "mobile ..." aside from the logo varying most of the sites look the same.    We want something different..

The following may be repetitive from our brief but here goes:

Banner will focus on 3 categories - SMS/Text Marketing, Mobile Websites and Mobile Marketing:  
#1)  Headline - Did you notice how many consumers are on smartphones today?  Reach them now. 
Sub text - Mobile coupons get 10 times the redemption rate of traditional coupons
Text messages are read by 94% of recipients within 4 minutes
50% of SMS users are aged 35+ 

#2) Headline - Every day 53% of Americans use their smartphone to search the web.  Do you have a mobile optimized website?   You could be missing all these consumers each day. 
Sub text - 95% of smarthphone users search for local information 
                         70% of all mobile searches result in action within 1 hour
#3) Headline - Break through the clutter - innovative marketing campaigns distinguish your brand
Sub text - Integrate social and mobile campaigns whenever and wherever
 91% of U.S. population have a mobile device within reach 24/7

** We are open to suggestions for images or style of banner - 

Below the banner would like to have a content section featuring rotating messages titled as:
  
DID YOU KNOW? }   There are 5 times as many texters as there are Chatterloop users?   < note 3-4 messages will scroll - a read more text link to an inner page for more of these facts.. 

Need 3 content sections - would prefer atypical format - not boxes, or framed areas but something different - titled:
What is a mobile website?  
Connect with mobile consumers
Mobile marketing revolution

Need:  
** a login icon for clients to access; contact us, email and text message optin - (see reference to Dravix and Quarvelworks sites from prior brief - dravix uses creative fonts for the contact us box and email /sms optin,  quarvelworks uses a creative call to action adjacent to the mobile phone with 3 options)

** to see active/ mouse over effect for navigation
** avoid a really long page - perhaps using scripts to reveal drop down boxes in content sections if necessary. 
** use of complimentary colors - keeping to white with elements of just black and green from logo gets boring
**  interesting yet not distracting shapes
** need to avoid bubble gum or flouorescent colors - note dravix mixes colors in the main banner area in an interesting fashion. 

** need frameless design  

Again, reference the sites we liked .. and didn't like on the original brief.  Additionally we also like these sites:

1) quenlo.example - open, expansive area - uncluttered,

2) http://presskit.harbordaily.example - love the layout and use of the black to emulate ink against white paper tying into the newspaper / brand.  We LOVE LOVE LOVE.. that sort of creativity.. in fact this is perhaps one of our favorite sites and how efficient and unique content sections, buttons, navigation, etc. is 

Looking forward to your submissions - cheers!!   

Reason: Attention all designers - this is the final extension! There are some great comps rolling in so PLEASE get your designs in soon !!!

Target Market(s)

Quite diverse actually - from local businesses (e.g., trades, professional services, retail, restaurant, hospitality, etc.) to agencies.

Industry/Entity Type

Progressive

Requirements
Must have
• Main banner of sort for messaging - would like to present 4-5 key messages that rotate/ fade on topics of SMS, mobile users, etc.
We were wondering if using mobile devices as palvexagency.example did to feature messages - but perhaps this limits amount of text. Also like the www.dravix.example site with the banner rotating but also revealing portions of the slide before and after.

3-4 sections to promote key content that link to inner pages. These will feature some text - e.g., see www.brindlecell.example - creative use of staggering box height and using script to reveal.

Main navigation = Home, Why Mobile, What We Do, Services, News (a blog), Contact. There will be 3-8 subpages for Why mobile, what we do, and services.

Footer - should contain email / text messaging sign up - see www.dravix.example for their optin in design.

Get in Touch- again, love how www.dravix.example has designed the "Get in Touch" call to action - not the typical button shape.

Blog - absolutely

Social icons - chatterloop , workhive, and..?
Nice to have
• Not sure what we'd need here - unless you have an idea. We're open to suggestions despite our strong opinions stated so far..
Should not have
• Avoid:
anything too extreme -
avoid cartoon type illustrations
heavy use of icons
extreme colors
font that is hard to read..

```html
<!DOCTYPE html>
<html lang="en">
<head>
<meta charset="utf-8">
<title>Tornacell — Mobile Marketing</title>
<link rel="stylesheet" href="https://fonts.googleapis.com/css2?family=Arimo:wght@400;700&family=Cabin:wght@700&display=swap">
<style>
:root{
  --green:#6cb33e;
  --green-dark:#4f9a2a;
  --ink:#333333;
  --ink-soft:#555555;
  --muted:#a7a7a7;
  --bar-top:#2e2e2e;
  --bar-bottom:#0d0d0d;
  --panel:#e3e3e3;
  --footer:#2f2f2f;
  --footer-text:#bdbdbd;
  --white:#ffffff;
}
*{box-sizing:border-box;margin:0;padding:0}
html,body{width:1190px;height:1200px;overflow:hidden}
body{font-family:"Arimo",Arial,sans-serif;color:var(--ink);background:var(--white);position:relative}
a{text-decoration:none;color:inherit}

.topbar{position:absolute;left:0;top:0;width:1190px;height:55px;background:linear-gradient(var(--bar-top),var(--bar-bottom));z-index:2}
.main-nav{position:absolute;left:126px;top:17px;display:flex;font-size:16px;font-weight:700}
.main-nav a{color:var(--green);padding:0 10px;border-left:1px solid #3d3d3d;line-height:20px}
.main-nav a:first-child{color:var(--white);padding-left:0;border-left:none}
.main-nav a:hover{color:var(--white)}
.social-top{position:absolute;left:752px;top:19px;display:flex;gap:14px;font-size:16px;font-weight:700;color:var(--white)}

.touch-badge{position:absolute;left:948px;top:-22px;width:128px;height:124px;border-radius:50%;background:radial-gradient(circle at 50% 40%,#3a3a3a,#161616);z-index:3;font-family:"Cabin",Arial,sans-serif;font-weight:700;color:#d9d9d9;text-align:center;padding-top:30px;line-height:32px;font-size:34px;letter-spacing:-1px}
.touch-badge span{display:block;color:#9a9a9a}

.hero{position:absolute;left:0;top:55px;width:1190px;height:610px;background:linear-gradient(#d2d5d7 0%,#e8eaeb 55%,#ffffff 100%)}
.brand{position:absolute;left:126px;top:50px}
.brand-name{font-size:48px;font-weight:700;color:var(--ink-soft);letter-spacing:-1px;line-height:50px}
.brand-tag{font-size:13px;letter-spacing:1.5px;color:var(--ink-soft);margin-left:12px}
.headline{position:absolute;left:129px;top:152px;font-size:47px;font-weight:700;line-height:51px;letter-spacing:-1.5px;color:var(--ink)}
.headline em{font-style:normal;color:var(--green)}
.cta-button{position:absolute;left:129px;top:377px;width:252px;height:55px;background:linear-gradient(#3a3a3a 0%,#1a1a1a 60%,#000 61%,#111 100%);color:var(--white);font-size:21px;font-weight:700;letter-spacing:-0.5px;display:flex;align-items:center;justify-content:center}
.cta-button em{font-style:normal;color:var(--green);margin-left:5px}

.device-showcase{position:absolute;left:433px;top:50px;width:660px;height:505px;border-radius:24px;background:linear-gradient(160deg,#1c1c1c 0%,#3a3a3a 60%,#d4d6d8 100%)}
.slide-screen{position:absolute;left:58px;top:56px;width:453px;height:329px;background:linear-gradient(135deg,#bdbdbd,#6a6a6a 60%,#4d4d4d)}
.slide-stat{position:absolute;left:31px;top:207px;color:#4a4a4a;font-weight:700}
.slide-stat strong{display:block;font-size:62px;line-height:56px;letter-spacing:-2px}
.slide-stat p{font-size:17px;line-height:15px;letter-spacing:-0.5px;width:200px}
.slide-dots{position:absolute;left:264px;top:398px;display:flex;gap:4px}
.slide-dots i{width:15px;height:15px;border-radius:50%;border:2px solid #5d5d5d;background:#222}
.slide-dots i.on{background:var(--green);box-shadow:inset 0 0 0 2px #222}

.features{position:absolute;left:0;top:665px;width:1190px}
.feature{position:absolute;top:0;width:265px}
.feature h2{font-size:22px;line-height:22px;color:var(--ink-soft);letter-spacing:-0.5px;height:48px;display:flex;align-items:flex-end}
.feature p{font-size:12.5px;line-height:17px;color:var(--ink);margin-top:4px}
.feature a{display:block;font-size:13px;font-weight:700;color:var(--green);margin-top:10px}

.lower{position:absolute;left:0;top:798px;width:1190px;height:228px;background:var(--panel);border-top:2px solid #cfcfcf}
.lower h3{font-size:24px;letter-spacing:-1.5px;color:var(--muted);font-weight:700}
.news-col{position:absolute;top:26px;width:282px}
.news-col p{font-size:11px;line-height:17px;color:#555;margin-top:16px}
.news-col h3+p{margin-top:6px}
.optin{position:absolute;left:761px;top:26px;width:270px}
.optin h3 svg{vertical-align:-2px}
.optin h4{font-size:14px;color:var(--ink-soft);margin:6px 0 6px}
.field{display:flex;gap:8px}
.field span{width:198px;height:27px;background:#cacaca;font-size:12px;color:#555;padding:7px 8px}
.field b{width:56px;height:27px;background:linear-gradient(#86cc55,var(--green-dark));color:var(--white);font-size:11px;font-weight:400;display:flex;align-items:center;justify-content:center;border-radius:2px}
.consent{display:flex;gap:9px;margin-top:11px;font-size:10px;line-height:12px;color:#555}
.consent svg{flex:none}

.footer{position:absolute;left:0;top:1026px;width:1190px;height:169px;background:var(--footer)}
.footer-col{position:absolute;top:30px}
.footer-col h4{font-size:16px;color:var(--white);margin-bottom:9px}
.footer-col p{font-size:11.5px;line-height:18px;color:var(--footer-text)}
.footer-social{display:flex;gap:20px;font-size:19px;font-weight:700;color:var(--green);margin-bottom:12px}
.contact-grid{display:grid;grid-template-columns:150px auto;font-size:11.5px;line-height:18px;color:var(--footer-text)}
.contact-grid b{color:var(--white);margin-right:6px}
.footer-line{position:absolute;left:0;top:1195px;width:1190px;height:5px;background:var(--green)}
</style>
</head>
<body>

<header class="topbar">
  <nav class="main-nav">
    <a href="#">Home</a><a href="#">Why Mobile</a><a href="#">What We Do</a><a href="#">Services</a><a href="#">News</a><a href="#">Contact</a>
  </nav>
  <div class="social-top"><a href="#">chatterloop</a><a href="#">chirpwave</a></div>
</header>
<a class="touch-badge" href="#">get in<span>touch</span></a>

<section class="hero">
  <div class="brand">
    <div class="brand-name">Tornacell</div>
    <div class="brand-tag">MAKE YOUR BRAND TORNA.CELL</div>
  </div>
  <h1 class="headline">We Build<br>Mobile<br>Applications<br>That <em>Matter</em></h1>
  <a class="cta-button" href="#">Open Your <em>Eyes</em></a>

  <div class="device-showcase" role="img" aria-label="Tablet and two smartphones displaying the brand mark and a rotating banner slide">
    <div class="slide-screen">
      <div class="slide-stat"><strong>70%</strong><p>of all mobile searches result in action within 1 hour</p></div>
    </div>
    <div class="slide-dots"><i></i><i class="on"></i><i></i><i></i><i></i></div>
  </div>
</section>

<section class="features">
  <article class="feature" style="left:125px">
    <h2>What is a mobile website?</h2>
    <p>Lorem ipsum dolor sit amet, consecteturadipi sicing elit, sed do eiusmod tempor incididunt</p>
    <a href="#">Check out what we have to offer</a>
  </article>
  <article class="feature" style="left:442px">
    <h2>Connect with mobile consumers</h2>
    <p>Lorem ipsum dolor sit amet, consecteturadipi sicing elit, sed do eiusmod tempor incididunt</p>
    <a href="#">Check out what we have to offer</a>
  </article>
  <article class="feature" style="left:761px">
    <h2>Mobile marketing revolution</h2>
    <p>Lorem ipsum dolor sit amet, consecteturadipi sicing elit, sed do eiusmod tempor incididunt</p>
    <a href="#">Check out what we have to offer</a>
  </article>
</section>

<section class="lower">
  <div class="news-col" style="left:124px">
    <h3>Recent Blog Posts</h3>
    <p>Lorem ipsum dolor sit amet, consectetur adipisicing elit, sed do eiusmod tempor incididunt</p>
    <p>ut labore et dolore magna aliqua. Ut enim ad minim veniam, quis nostrud exercitation ullamco</p>
    <p>laboris nisi ut aliquip ex ea commodo consequat. Duis aute irure dolor in</p>
  </div>
  <div class="news-col" style="left:441px">
    <h3>Recent News</h3>
    <p>Lorem ipsum dolor sit amet, consectetur adipisicing elit, sed do eiusmod tempor incididunt</p>
    <p>ut labore et dolore magna aliqua. Ut enim ad minim veniam, quis nostrud exercitation ullamco</p>
    <p>laboris nisi ut aliquip ex ea commodo consequat. Duis aute irure dolor in</p>
  </div>
  <div class="optin">
    <h3>Get in touch <svg width="13" height="22" viewBox="0 0 13 22"><rect x="1" y="1" width="11" height="20" rx="2" fill="none" stroke="#a7a7a7" stroke-width="1.5"/><rect x="3" y="4" width="7" height="12" fill="#a7a7a7"/></svg></h3>
    <h4>Receceive Our Monthly Newsletter</h4>
    <div class="field"><span>email</span><b>submit</b></div>
    <h4 style="margin-top:11px">Get Dravix Text Alerts</h4>
    <div class="field"><span>phone</span><b>submit</b></div>
    <div class="consent">
      <svg width="14" height="14" viewBox="0 0 14 14"><rect x="0.5" y="0.5" width="13" height="13" rx="2" fill="#f2f2f2" stroke="#b5b5b5"/><path d="M3.5 7.2l2.3 2.3 4.6-5" fill="none" stroke="#666" stroke-width="1.4"/></svg>
      <span>I understand standard message rates<br>of my carrier may apply.</span>
    </div>
  </div>
</section>

<footer class="footer">
  <div class="footer-col" style="left:124px">
    <h4>Why Mobile</h4>
    <p>Lorem ipsum dolor sit<br>ea commodo con<br>veniam, quis nostolor in<br>Lorem ipsum dolor sit<br>ea commodo con</p>
  </div>
  <div class="footer-col" style="left:290px">
    <h4>What We Do</h4>
    <p>Lorem ipsum dolor sit<br>ea commodo con<br>veniam, quis nostolor in<br>Lorem ipsum dolor sit<br>ea commodo con</p>
  </div>
  <div class="footer-col" style="left:442px">
    <h4>Services</h4>
    <p>Lorem ipsum dolor sit<br>ea commodo con<br>veniam, quis nostolor in<br>Lorem ipsum dolor sit<br>ea commodo con</p>
  </div>
  <div class="footer-col" style="left:601px">
    <h4>News</h4>
    <p>Lorem ipsum dolor sit<br>ea commodo con<br>veniam, quis nostolor in<br>Lorem ipsum dolor sit<br>ea commodo con</p>
  </div>
  <div class="footer-col" style="left:764px">
    <h4>Keep in Touch</h4>
    <div class="footer-social"><a href="#">chatterloop</a><a href="#">chirpwave</a></div>
    <div class="contact-grid">
      <span>Address, City, Country</span><span><b>T</b>555.555.5555</span>
      <span>555 Street Name</span><span><b>F</b>666.666.6666</span>
      <span>City, State. 90213</span><span><b>T</b>1.800.555.6666</span>
    </div>
  </div>
</footer>
<div class="footer-line"></div>

</body>
</html>
```